New Coffee Shop business card

We are opening our new coffee shop and are needing business cards to take with us on February 6th to Atlanta, Ga to a show.

We will be offering the following menu type items:

coffee
teas
espresso
frappes
smoothies

sandwiches
soups
salads
pastries
ice cream

Our shop is in a rural country-side area and we would like to convey that feel in our shop. In addition to the cafe we will also be selling gifts and furniture and other home decor. Much of this merchandise will be rescued, refurbished or repurposed which is also a core value of what we are all about.

We have a company logo we would like incorporated into the design.

We will also provide files that have the elements of the logo which may also be useful in the design of the card.

Since we are not open yet we need one slightly altered version of the card as well as the final product which states "Opening in the summer 2015"

Target Market(s)

moderate to slightly upscale and folksy.

Industry/Entity Type

Coffee Shop

Contact Information for Business Card

Fern Hollow Coffee
name
address
phone number
email

Card

Font styles to use
Sans Serif

Requirements
Must have
• Must include Logo
• Must include information on menu.
• Must include information on our merchandise sales as described inthe project description.
• Color scheme to complement the logo
Nice to have
• The following descriptions
• "We are also selling gifts, furniture, and other home decoration."
• "We rescue, refurbish, and repurpose old furniture so it can live again."

```html
<!DOCTYPE html>
<html lang="en">
<head>
<meta charset="utf-8">
<title>Fern Hollow Coffee – Business Cards</title>
<link href="https://fonts.googleapis.com/css2?family=Jost:wght@400;500&display=swap" rel="stylesheet">
<style>
  :root {
    --backdrop: #cfcfcf;
    --card: #0a0a0a;
    --edge-text: #8c8c8c;
    --body-text: #f2f2f2;
    --accent-red: #a8353b;
    --frame: #c8b596;
    --menu-text: #ede6da;
  }
  * { box-sizing: border-box; margin: 0; padding: 0; }
  html, body {
    width: 1200px; height: 900px; overflow: hidden;
    background: var(--backdrop);
    font-family: "Jost", "Futura", sans-serif;
  }
  .canvas { position: relative; width: 1200px; height: 900px; }

  .card {
    position: absolute; width: 522px; height: 290px;
    background: var(--card); overflow: hidden;
    box-shadow: 0 6px 16px rgba(0,0,0,.35);
  }
  .card--front { left: 70px; top: 60px; }
  .card--opening { left: 615px; top: 172px; }
  .card--back { left: 412px; top: 520px; }

  .edge { position: absolute; color: var(--edge-text); font-size: 13.5px; white-space: nowrap; letter-spacing: .2px; }
  .edge--top { top: 7px; left: 0; right: 0; text-align: center; }
  .edge--bottom { bottom: 7px; left: 0; right: 0; text-align: center; transform: rotate(180deg); }
  .edge--left { left: 6px; top: 24px; height: 250px; writing-mode: vertical-rl; transform: rotate(180deg); text-align: center; }
  .edge--right { right: 6px; top: 24px; height: 250px; writing-mode: vertical-rl; text-align: center; }

  .brand {
    position: absolute; left: 0; right: 0; top: 100px;
    display: flex; align-items: center; justify-content: center; gap: 14px;
  }
  .brand__dot { width: 22px; height: 22px; border-radius: 50%; background: var(--accent-red); }
  .brand__name { color: var(--body-text); font-size: 34px; font-weight: 400; }

  .content { position: absolute; left: 30px; width: 350px; text-align: center; color: var(--body-text); }
  .card--opening .content { top: 34px; }
  .card--back .content { top: 58px; }
  .headline { font-size: 27px; font-weight: 400; letter-spacing: .6px; white-space: nowrap; margin-left: -8px; width: 440px; text-align: center; margin-bottom: 6px; }
  .blurb { font-size: 16px; line-height: 19px; margin-bottom: 9px; }
  .phone-icon { display: block; margin: 10px auto 2px; width: 20px; height: 14px; }
  .phone { font-size: 21px; letter-spacing: .5px; line-height: 24px; }
  .address, .email { color: var(--accent-red); font-size: 14px; line-height: 18px; }

  .menu { position: absolute; left: 382px; width: 100px; height: 162px; }
  .card--opening .menu { top: 84px; }
  .card--back .menu { top: 72px; }
  .menu svg { position: absolute; inset: 0; }
  .menu__list { position: relative; list-style: none; text-align: center; padding-top: 9px; color: var(--menu-text); font-size: 12.5px; line-height: 15.2px; }
  .menu__title { color: var(--accent-red); font-weight: 500; font-size: 12.5px; }
</style>
</head>
<body>
<div class="canvas">

  <!-- Front -->
  <section class="card card--front">
    <div class="edge edge--top">• coffee • gifts • furniture • home decor • coffee • gifts • furniture</div>
    <div class="edge edge--left">home decor • coffee • gifts</div>
    <div class="edge edge--right">home decor • coffee • gifts</div>
    <div class="edge edge--bottom">furniture • home decor • coffee • gifts • furniture • home decor •</div>
    <div class="brand">
      <span class="brand__dot"></span>
      <span class="brand__name">Fern Hollow Coffee</span>
    </div>
  </section>

  <!-- Opening announcement -->
  <section class="card card--opening">
    <div class="edge edge--top">• coffee • gifts • furniture • home decor • coffee • gifts • furniture</div>
    <div class="edge edge--left">home decor • coffee • gifts</div>
    <div class="edge edge--right">home decor • coffee • gifts</div>
    <div class="edge edge--bottom">furniture • home decor • coffee • gifts • furniture • home decor •</div>
    <div class="content">
      <h1 class="headline">OPENING IN THE SUMMER 2015</h1>
      <p class="blurb">We are also selling gifts, furniture, and other home decoration.</p>
      <p class="blurb">We rescue, refurbish, and repurpose old furniture so it can live again.</p>
      <svg class="phone-icon" viewBox="0 0 20 14" aria-hidden="true"><path d="M1 4 Q10 -1 19 4 L17 6 L14 5 L14 3 Q10 2 6 3 L6 5 L3 6 Z M5 6 H15 L17 13 H3 Z" fill="#f2f2f2"/><circle cx="10" cy="9.5" r="2" fill="#0a0a0a"/></svg>
      <p class="phone">1404 5 555 018</p>
      <p class="address">18 Mill Creek Rd Ste 4, Atlanta GA 30303</p>
      <p class="email">info@fernhollow.com</p>
    </div>
    <div class="menu">
      <svg viewBox="0 0 100 162" aria-hidden="true"><path d="M9 1.5 H91 A8 8 0 0 0 98.5 9 V153 A8 8 0 0 0 91 160.5 H9 A8 8 0 0 0 1.5 153 V9 A8 8 0 0 0 9 1.5 Z" fill="none" stroke="var(--frame)" stroke-width="2"/></svg>
      <ul class="menu__list">
        <li class="menu__title">MENU:</li>
        <li>coffee &nbsp;teas</li><li>espresso</li><li>frappes</li><li>smoothies</li><li>sandwiches</li><li>soups</li><li>salads</li><li>pastries</li><li>ice cream</li>
      </ul>
    </div>
  </section>

  <!-- Back -->
  <section class="card card--back">
    <div class="edge edge--top">• coffee • gifts • furniture • home decor • coffee • gifts • furniture</div>
    <div class="edge edge--left">home decor • coffee • gifts</div>
    <div class="edge edge--right">home decor • coffee • gifts</div>
    <div class="edge edge--bottom">furniture • home decor • coffee • gifts • furniture • home decor •</div>
    <div class="content">
      <p class="blurb">We are also selling gifts, furniture, and other home decoration.</p>
      <p class="blurb">We rescue, refurbish, and repurpose old furniture so it can live again.</p>
      <svg class="phone-icon" viewBox="0 0 20 14" aria-hidden="true"><path d="M1 4 Q10 -1 19 4 L17 6 L14 5 L14 3 Q10 2 6 3 L6 5 L3 6 Z M5 6 H15 L17 13 H3 Z" fill="#f2f2f2"/><circle cx="10" cy="9.5" r="2" fill="#0a0a0a"/></svg>
      <p class="phone">1404 5 555 018</p>
      <p class="address">18 Mill Creek Rd Ste 4, Atlanta GA 30303</p>
      <p class="email">info@fernhollow.com</p>
    </div>
    <div class="menu">
      <svg viewBox="0 0 100 162" aria-hidden="true"><path d="M9 1.5 H91 A8 8 0 0 0 98.5 9 V153 A8 8 0 0 0 91 160.5 H9 A8 8 0 0 0 1.5 153 V9 A8 8 0 0 0 9 1.5 Z" fill="none" stroke="var(--frame)" stroke-width="2"/></svg>
      <ul class="menu__list">
        <li class="menu__title">MENU:</li>
        <li>coffee &nbsp;teas</li><li>espresso</li><li>frappes</li><li>smoothies</li><li>sandwiches</li><li>soups</li><li>salads</li><li>pastries</li><li>ice cream</li>
      </ul>
    </div>
  </section>

</div>
</body>
</html>
```